Business Card Design

Motorvane Ledger is an online automotive resource on a national scale specifically targeting lease purchases for new cars. Our Online and app platform allow prospective lease clients to scan a window sticker while at a franchise dealership and instantly receive a lease quote at what we call the sweet spot. Motorvane Ledger offers price transparency during the lease process to allow average people the confidence in the lease process and takes away any fear of the big franchise dealers.
Motorvane ledger allows ordinary lease customers to know they are getting a low price lease and not overpaying. Never overpay again

Industry/Entity Type

Automotive

Contact Information for Business Card

Motorvane Ledger
Martin Sowerby (President of operations)
Phone: 888-247-6031
Cell: 561-384-2706

```html
<!DOCTYPE html>
<html lang="en">
<head>
<meta charset="utf-8">
<title>Motorvane Ledger – Business Card</title>
<link rel="stylesheet" href="https://fonts.googleapis.com/css2?family=Montserrat:wght@300;700;900&display=swap">
<style>
  :root {
    --backdrop: #2c2c2e;
    --card-black: #161617;
    --card-charcoal: #2a2a2c;
    --paper-white: #ffffff;
    --ink-black: #111111;
    --muted-white: #e6e6e6;
  }
  * { box-sizing: border-box; margin: 0; padding: 0; }
  html, body {
    width: 1200px; height: 819px; overflow: hidden;
    background: var(--backdrop);
    font-family: "Montserrat", Arial, sans-serif;
  }
  .stage {
    position: relative; width: 1200px; height: 819px;
  }
  .card {
    position: absolute; top: 261px;
    width: 520px; height: 297px;
    overflow: hidden;
    box-shadow: 0 12px 30px rgba(0,0,0,.45);
  }

  /* Back side: black with name mark */
  .card--back {
    left: 50px;
    background: var(--card-black);
  }
  .card--back .wordmark {
    position: absolute; left: 60px; top: 108px;
    color: var(--paper-white);
  }

  /* Wordmark: plain circle + stacked name, one weight, one colour */
  .wordmark {
    display: flex; align-items: center; gap: 16px;
  }
  .wordmark__dot {
    width: 62px; height: 62px; border-radius: 50%;
    background: currentColor; flex: none;
  }
  .wordmark__name {
    font-weight: 900; text-transform: uppercase;
    font-size: 40px; line-height: 0.95; letter-spacing: -0.5px;
  }
  .wordmark__name span { display: block; }
  .wordmark__name span:first-child { padding-left: 4px; }

  /* Front side: white band above, charcoal below */
  .card--front {
    left: 630px;
    background: var(--card-charcoal);
  }
  .front__band {
    position: absolute; left: 0; top: 0; width: 100%; height: 150px;
    background: var(--paper-white);
  }
  .front__rule {
    position: absolute; left: 0; top: 160px; width: 100%; height: 3px;
    background: var(--paper-white);
  }
  .card--front .wordmark {
    position: absolute; right: 24px; top: 46px;
    color: var(--ink-black);
  }
  .contact {
    position: absolute; left: 28px; top: 186px;
    color: var(--paper-white);
  }
  .contact__name {
    font-weight: 700; font-size: 19px; text-transform: uppercase; letter-spacing: 0.3px;
  }
  .contact__title {
    font-weight: 300; font-size: 14px; margin-top: 2px; color: var(--muted-white);
  }
  .contact__list { list-style: none; margin-top: 8px; }
  .contact__item {
    display: flex; align-items: center; gap: 10px;
    font-weight: 300; font-size: 15px; line-height: 22px; color: var(--muted-white);
  }
  .contact__icon { width: 12px; height: 14px; flex: none; }
</style>
</head>
<body>
<main class="stage">

  <section class="card card--back" aria-label="Business card, back">
    <div class="wordmark">
      <span class="wordmark__dot" aria-hidden="true"></span>
      <p class="wordmark__name"><span>Motorvane</span><span>Ledger</span></p>
    </div>
  </section>

  <section class="card card--front" aria-label="Business card, front">
    <div class="front__band"></div>
    <div class="front__rule"></div>
    <div class="wordmark">
      <span class="wordmark__dot" aria-hidden="true"></span>
      <p class="wordmark__name"><span>Motorvane</span><span>Ledger</span></p>
    </div>
    <div class="contact">
      <p class="contact__name">Martin Sowerby</p>
      <p class="contact__title">President of operations</p>
      <ul class="contact__list">
        <li class="contact__item">
          <svg class="contact__icon" viewBox="0 0 12 14" aria-label="Mobile">
            <rect x="2" y="0.5" width="8" height="13" rx="1.5" fill="none" stroke="#e6e6e6" stroke-width="1.2"/>
            <circle cx="6" cy="11.2" r="0.8" fill="#e6e6e6"/>
          </svg>
          888-247-6031
        </li>
        <li class="contact__item">
          <svg class="contact__icon" viewBox="0 0 12 14" aria-label="Phone">
            <path d="M1 5 Q6 1 11 5 L9.5 6.5 L8 5 L4 5 L2.5 6.5 Z" fill="#e6e6e6"/>
            <rect x="2" y="7" width="8" height="6" rx="1" fill="#e6e6e6"/>
          </svg>
          561-384-2706
        </li>
      </ul>
    </div>
  </section>

</main>
</body>
</html>
```